Summer Adventure Day - Poster design

Our company is based in the West End of Glasgow. During the summer holidays every weekday we are running a number of Adventure Days for young people aged 8+. The dates are from Monday 2nd July through to Friday 10th August. The activities vary each day but include climbing, hillwalking, bushcraft, kayaking, archery, abseiling and orienteering. The activities run from 8:30am to 4:30pm, and the drop off / pick up location is 14 Tarbet Crescent, Ashcroft, Glasgow, G31 7QN.
We are looking for an eye catching poster design that advertises the summer holiday adventure days. We are also needing the poster to be easily adaptable for both our Chatterly header and to run promotions on Chatterly. For more information on what we do and for some photos see our chatterly page - Brightmoor Outdoor Club.

The poster needs to include our logo, the QNRB logo and the YTQA Logo all attached to this brief. The poster needs to direct people to our website to book www.brightmooroutdoorclub.co.uk
The final design should be bright, colorful, eye catching and make people want to book onto either an adventure day or an adventure week.

The poster should also be easily adaptable to landscape for a billboard as well as portrait for a magazine advert.

Target Market(s)

Parents of children aged 8+

Colors

Designer to choose colors to be used in the design.

Requirements
Must have
• The project must contain our logo, our website address, how to book along with information on what is happening. The poster should also be easily adaptable for both our Chatterly header and to be able to use for a Chatterly Advert.
Nice to have
• S0me of the photos from the previous adventure weeks, photos can be found on our chatterly page - Brightmoor Outdoor Club. Should be bright and colourful and attract more business to our website.
Should not have
• Our mailing address it should be the address for pick up / drop off

```html
<!DOCTYPE html>
<html lang="en">
<head>
<meta charset="utf-8">
<title>Adventure Days – Brightmoor Outdoor Club</title>
<link rel="stylesheet" href="https://fonts.googleapis.com/css2?family=Bangers&family=Open+Sans:ital,wght@0,400;0,600;0,700;1,800&display=swap">
<style>
  :root {
    --orange: #f28a30;
    --cream: #fde3c6;
    --ink: #1d1d1b;
    --white: #ffffff;
  }
  * { margin: 0; padding: 0; box-sizing: border-box; }
  html, body { width: 848px; height: 1200px; overflow: hidden; background: var(--orange); }
  .poster {
    position: relative; width: 848px; height: 1200px; overflow: hidden;
    background: var(--orange);
    font-family: "Open Sans", sans-serif; color: var(--white);
  }
  .poster-art { position: absolute; inset: 0; }
  .title { font-family: "Bangers", cursive; fill: var(--ink); }
  .activities { font-family: "Open Sans", sans-serif; font-size: 17px; fill: var(--white); letter-spacing: 0.5px; }
  .age { font-family: "Open Sans", sans-serif; font-weight: 800; font-style: italic; font-size: 86px; fill: var(--white); }
  .intro, .range, .daily, .dropoff, .club-name, .website {
    position: absolute; left: 0; width: 848px; text-align: center; white-space: nowrap;
  }
  .intro { top: 638px; font-size: 18.5px; color: var(--ink); letter-spacing: 0.3px; }
  .range { top: 668px; font-size: 37px; font-weight: 400; letter-spacing: 1px; }
  .range-rule { position: absolute; top: 714px; left: 100px; width: 648px; height: 2px; background: var(--cream); }
  .daily { top: 726px; font-size: 18px; color: var(--ink); letter-spacing: 0.1px; }
  .photo-frame {
    position: absolute; top: 757px; width: 211px; height: 221px;
    border: 3px solid var(--white); border-radius: 12px;
  }
  .photo-left { left: 38px; background: linear-gradient(165deg, #9fbfe0 0%, #c9d3da 25%, #6d6a5e 50%, #c43a3a 68%, #3a7ec4 82%, #3b3632 100%); }
  .photo-right { left: 612px; background: linear-gradient(170deg, #5e97d8 0%, #a9c2de 30%, #8a7d66 50%, #d23b3b 66%, #8f8c84 80%, #3f8a4a 100%); }
  .dates { position: absolute; left: 264px; top: 798px; font-size: 32px; line-height: 47px; white-space: nowrap; }
  .times { position: absolute; left: 265px; top: 900px; font-size: 21px; white-space: nowrap; }
  .dropoff { top: 990px; font-size: 17.2px; color: var(--ink); letter-spacing: 0.1px; }
  .club-name { top: 1078px; font-size: 28px; font-weight: 700; color: var(--ink); }
  .website { top: 1156px; font-size: 27.5px; font-weight: 600; color: var(--ink); letter-spacing: 0.4px; }
</style>
</head>
<body>
<main class="poster">
  <svg class="poster-art" width="848" height="1200" viewBox="0 0 848 1200" xmlns="http://www.w3.org/2000/svg">
    <defs>
      <clipPath id="heroClip"><polygon points="0,0 848,0 848,136 0,600"/></clipPath>
      <linearGradient id="heroBase" x1="0" y1="0" x2="1" y2="0.6">
        <stop offset="0" stop-color="#d84a50"/>
        <stop offset="0.45" stop-color="#c0303a"/>
        <stop offset="1" stop-color="#6a4a3a"/>
      </linearGradient>
      <radialGradient id="heroLight" cx="0.5" cy="0.5" r="0.5">
        <stop offset="0" stop-color="#e9b59a" stop-opacity="0.85"/>
        <stop offset="1" stop-color="#e9b59a" stop-opacity="0"/>
      </radialGradient>
      <radialGradient id="heroGreen" cx="0.5" cy="0.5" r="0.5">
        <stop offset="0" stop-color="#2f5a2e" stop-opacity="0.9"/>
        <stop offset="1" stop-color="#2f5a2e" stop-opacity="0"/>
      </radialGradient>
      <radialGradient id="heroShade" cx="0.5" cy="0.5" r="0.5">
        <stop offset="0" stop-color="#1f2230" stop-opacity="0.8"/>
        <stop offset="1" stop-color="#1f2230" stop-opacity="0"/>
      </radialGradient>
      <linearGradient id="portraitTone" x1="0" y1="0" x2="0.4" y2="1">
        <stop offset="0" stop-color="#3d78c4"/>
        <stop offset="0.35" stop-color="#7a6a5c"/>
        <stop offset="0.6" stop-color="#e7b29c"/>
        <stop offset="1" stop-color="#2aa3c8"/>
      </linearGradient>
    </defs>

    <!-- hero photograph area -->
    <g clip-path="url(#heroClip)" role="img" aria-label="Photo of a young boy in a red waterproof jacket pulling on his rucksack straps">
      <rect width="848" height="600" fill="url(#heroBase)"/>
      <ellipse cx="440" cy="170" rx="210" ry="190" fill="url(#heroLight)"/>
      <ellipse cx="420" cy="380" rx="170" ry="130" fill="url(#heroGreen)"/>
      <ellipse cx="150" cy="430" rx="200" ry="170" fill="url(#heroShade)"/>
      <ellipse cx="760" cy="60" rx="150" ry="110" fill="url(#heroShade)"/>
    </g>

    <!-- cream brushed frame -->
    <path d="M0,0 L848,0 L848,14 L600,8 L320,16 L60,10 L0,18 Z" fill="var(--cream)" opacity="0.8"/>
    <path d="M0,0 L20,0 L14,200 L22,420 L10,600 L0,600 Z" fill="var(--cream)" opacity="0.55"/>
    <path d="M826,150 L848,134 L848,1200 L832,1200 L838,920 L824,640 L836,380 Z" fill="var(--cream)" opacity="0.9"/>
    <path d="M0,600 L14,594 L8,860 L16,1200 L0,1200 Z" fill="var(--cream)" opacity="0.85"/>

    <!-- cream footer band -->
    <path d="M0,1020 L90,1012 L180,1024 L300,1010 L420,1022 L560,1008 L700,1020 L848,1010 L848,1200 L0,1200 Z" fill="var(--cream)"/>
    <path d="M40,1040 L260,1034 L250,1040 L40,1046 Z M520,1044 L800,1036 L800,1042 L520,1050 Z" fill="var(--orange)" opacity="0.5"/>

    <!-- title -->
    <text class="title" font-size="132" transform="translate(40,642) rotate(-30.5)" textLength="890" lengthAdjust="spacingAndGlyphs">ADVENTURE DAYS</text>

    <!-- activity list -->
    <text class="activities" transform="translate(64,678) rotate(-30.5)" textLength="832" lengthAdjust="spacingAndGlyphs">CLIMBING- HILLWALKING-BUSHCRAFT-KAYAKING-ARCHERY-ABSEILING-ORIENTEERING</text>

    <!-- age -->
    <text class="age" x="402" y="598">8+</text>

    <!-- circular portrait -->
    <circle cx="666" cy="518" r="108" fill="var(--white)"/>
    <circle cx="666" cy="518" r="103" fill="url(#portraitTone)" role="img" aria-label="Photo of a smiling girl wearing a climbing helmet"/>

    <!-- partner badges -->
    <circle cx="124" cy="1096" r="64" fill="none" stroke="var(--ink)" stroke-width="2" role="img" aria-label="QNRB badge"/>
    <rect x="686" y="1030" width="86" height="134" fill="var(--ink)" role="img" aria-label="YTQA approved provider badge"/>
  </svg>

  <p class="intro">BRIGHTMOOR OUTDOOR CLUB ARE PROVIDING</p>
  <h1 class="range">AN EXCITING RANGE OF ACTIVITIES</h1>
  <div class="range-rule"></div>
  <p class="daily">DAILY FROM OUR BASE IN THE WEST END OF GLASGOW DURING SUMMER HOLIDAYS</p>

  <div class="photo-frame photo-left" role="img" aria-label="Photo of a group of children sitting on rocks on a hillside"></div>
  <div class="photo-frame photo-right" role="img" aria-label="Photo of children posing on a boulder in the hills"></div>

  <p class="dates">Monday 2nd July to<br>Friday 10th August</p>
  <p class="times">from 8:30am to 4:30pm</p>

  <p class="dropoff">DROP OFF / PICK UP LOCATION IS 14 TARBET CRESCENT, ASHCROFT, GLASGOW, G31 7QN</p>

  <p class="club-name">Brightmoor Outdoor Club</p>
  <p class="website">www.brightmooroutdoorclub.co.uk</p>
</main>
</body>
</html>
```